the halvorsen group premier division

design a DL A4 tri fold brochure to reflect our creative landscape business
my web site www.thehalvorsengroup.com.au
has all the information needed
i will also be updating the website to be more updated and creative design

```html
<!DOCTYPE html>
<html lang="en">
<head>
<meta charset="utf-8">
<title>The Halvorsen Group – Tri-fold Brochure</title>
<link rel="stylesheet" href="https://fonts.googleapis.com/css2?family=Righteous&family=Josefin+Sans:wght@600;700&family=Poiret+One&family=Caveat+Brush&display=swap">
<style>
  :root {
    --orange: #e8892c;
    --orange-deep: #cf6a12;
    --orange-light: #eba43e;
    --charcoal: #4b4b4b;
    --charcoal-dark: #3c3c3c;
    --paper: #f2f2f2;
    --paper-shade: #e8e8e8;
    --ink: #4f4f55;
    --stage: #d9d9de;
  }
  * { box-sizing: border-box; margin: 0; padding: 0; }
  html, body { width: 1200px; height: 900px; overflow: hidden; }
  body {
    background: var(--stage);
    font-family: "Josefin Sans", sans-serif;
    position: relative;
  }
  .spread {
    position: absolute;
    left: 315px;
    width: 570px;
    height: 403px;
    box-shadow: 0 6px 18px rgba(0,0,0,.18);
    background: var(--paper);
  }
  .spread--outside { top: 24px; }
  .spread--inside { top: 463px; }
  .spread-art { position: absolute; inset: 0; width: 570px; height: 403px; display: block; }
  .panel {
    position: absolute;
    top: 0;
    width: 190px;
    height: 403px;
    padding: 0 14px;
  }
  .panel--1 { left: 0; }
  .panel--2 { left: 190px; }
  .panel--3 { left: 380px; }

  .heading {
    font-family: "Righteous", sans-serif;
    text-transform: uppercase;
    letter-spacing: 1.5px;
    text-align: center;
  }
  .body-copy {
    font-weight: 700;
    text-transform: uppercase;
    font-size: 6.4px;
    line-height: 1.6;
    letter-spacing: .4px;
  }

  /* outside: contact */
  .contact-title { color: var(--orange); font-size: 17px; margin-top: 28px; }
  .contact-name {
    position: absolute; top: 96px; left: 0; width: 190px;
    color: #fff; font-size: 11px; letter-spacing: 1.2px;
  }
  .contact-list { position: absolute; top: 124px; left: 16px; list-style: none; color: #fff; }
  .contact-item {
    display: flex; align-items: center; gap: 10px;
    font-family: "Righteous", sans-serif; text-transform: uppercase;
    font-size: 8px; letter-spacing: .8px; margin-bottom: 10px; line-height: 1.35;
  }
  .contact-item--small { font-size: 5.6px; letter-spacing: .4px; }
  .contact-icon { width: 14px; height: 14px; flex: none; }

  /* outside: about */
  .about-title { color: var(--orange); font-size: 16px; margin-top: 34px; margin-bottom: 14px; }
  .about-copy p { color: var(--orange); margin-bottom: 8px; }

  /* outside: cover */
  .cover-name {
    position: absolute; top: 120px; left: 0; width: 190px;
    text-align: center; color: var(--ink);
    font-weight: 700; font-size: 15px; line-height: 1.25;
  }
  .cover-name span { display: block; font-size: 6.5px; letter-spacing: 3px; text-transform: uppercase; }

  /* inside: intro */
  .intro-title { position: absolute; top: 212px; left: 22px; color: var(--ink); }
  .intro-word { font-family: "Righteous", sans-serif; text-transform: uppercase; font-size: 17px; letter-spacing: 2px; display: block; }
  .intro-to { font-family: "Caveat Brush", cursive; color: var(--orange); font-size: 24px; display: block; margin-left: 38px; line-height: 1; }
  .intro-accent { font-family: "Poiret One", cursive; color: var(--orange); font-size: 30px; display: block; letter-spacing: 1px; }

  /* inside: services */
  .services-title { font-size: 16px; margin-top: 32px; margin-bottom: 14px; color: var(--ink); }
  .services-title em { font-style: normal; color: var(--orange); }
  .service { margin-bottom: 26px; }
  .service-name {
    color: var(--orange); font-size: 9.5px; line-height: 1.2;
    padding-bottom: 5px; margin: 0 16px 7px;
    border-bottom: 1px solid var(--ink);
  }
  .service-copy { color: var(--ink); text-align: center; }
</style>
</head>
<body>

<!-- Outside of the brochure -->
<section class="spread spread--outside" aria-label="Brochure outside">
  <svg class="spread-art" viewBox="0 0 570 403" aria-hidden="true">
    <defs>
      <linearGradient id="bandOrange" x1="0" y1="0" x2="1" y2="1">
        <stop offset="0" stop-color="#e8892c"/>
        <stop offset="1" stop-color="#cf6a12"/>
      </linearGradient>
      <linearGradient id="charcoalFade" x1="0" y1="0" x2="0" y2="1">
        <stop offset="0" stop-color="#5a5a5a"/>
        <stop offset="1" stop-color="#3c3c3c"/>
      </linearGradient>
    </defs>
    <rect x="0" y="0" width="190" height="403" fill="#f2f2f2"/>
    <polygon points="0,68 190,92 190,252 0,210" fill="url(#bandOrange)"/>
    <rect x="190" y="0" width="190" height="403" fill="url(#charcoalFade)"/>
    <rect x="380" y="0" width="190" height="403" fill="#efefef"/>
    <path d="M240 403 Q380 285 570 292 L570 403 Z" fill="#555555"/>
    <path d="M300 403 Q430 312 570 312 L570 403 Z" fill="#e38a3c"/>
    <path d="M395 403 Q470 335 570 330 L570 403 Z" fill="#eba43e"/>
  </svg>

  <div class="panel panel--1">
    <h2 class="heading contact-title">Contact</h2>
    <p class="heading contact-name">Ivar Lindqvist</p>
    <ul class="contact-list">
      <li class="contact-item">
        <svg class="contact-icon" viewBox="0 0 24 24" fill="none" stroke="#fff" stroke-width="1.6"><path d="M6 3l3 4-2 2c1 3 4 6 7 7l2-2 4 3-2 4C10 20 4 14 3 5z"/></svg>
        0412 88 30 61
      </li>
      <li class="contact-item">
        <svg class="contact-icon" viewBox="0 0 24 24" fill="none" stroke="#fff" stroke-width="1.6"><path d="M12 22s7-7 7-12a7 7 0 0 0-14 0c0 5 7 12 7 12z"/><circle cx="12" cy="10" r="2.5"/></svg>
        PO Box 742,<br>Northcote 3070
      </li>
      <li class="contact-item contact-item--small">
        <svg class="contact-icon" viewBox="0 0 24 24" fill="none" stroke="#fff" stroke-width="1.6"><rect x="3" y="6" width="18" height="12"/><path d="M3 6l9 7 9-7"/></svg>
        ivar@thehalvorsengroup.com.au
      </li>
      <li class="contact-item contact-item--small">
        <svg class="contact-icon" viewBox="0 0 24 24" fill="none" stroke="#fff" stroke-width="1.6"><circle cx="12" cy="12" r="9"/><path d="M3 12h18M12 3c3 3 3 15 0 18M12 3c-3 3-3 15 0 18"/></svg>
        www.thehalvorsengroup.com.au
      </li>
    </ul>
  </div>

  <div class="panel panel--2">
    <h2 class="heading about-title">About Us</h2>
    <div class="about-copy body-copy">
      <p>The Halvorsen Group (THG), formerly Ivar Lindqvist Landscapes, is a professional landscaping and construction service that takes pride in delivering high-end outdoor landscapes across Melbourne.</p>
      <p>Victoria. Ivar Lindqvist, head of the Halvorsen Group, offers a team that dedicates their efforts from concept development to installation and maintenance to ensure the outdoor creation becomes part of the client's home and life experience with visual, tactile and sensory inclusions.</p>
      <p>Over its 20 years, the business has developed a strong reputation for positive customer experiences, innovative designs and quality outcomes to suit individual needs and design styles. When working with Ivar Lindqvist's team, you work with a qualified ensemble of experienced landscapers and horticultural</p>
    </div>
  </div>

  <div class="panel panel--3">
    <p class="cover-name">The Halvorsen Group<span>Premier Division</span></p>
  </div>
</section>

<!-- Inside of the brochure -->
<section class="spread spread--inside" aria-label="Brochure inside">
  <svg class="spread-art" viewBox="0 0 570 403" aria-hidden="false">
    <rect x="0" y="0" width="190" height="403" fill="#f3f3f3"/>
    <rect x="190" y="0" width="190" height="403" fill="#eeeeee"/>
    <rect x="380" y="0" width="190" height="403" fill="#e7e7e7"/>
    <polygon points="0,110 110,150 0,190" fill="#e8943a"/>
    <linearGradient id="photoTone" x1="0" y1="0" x2="0" y2="1">
      <stop offset="0" stop-color="#8ea3c9"/>
      <stop offset="0.55" stop-color="#d8c6a6"/>
      <stop offset="1" stop-color="#3d8fc4"/>
    </linearGradient>
    <polygon role="img" aria-label="Photo of a large home with a lit pool and garden at dusk" points="32,0 190,0 190,218 0,140 0,72" fill="url(#photoTone)"/>
    <path d="M130 403 Q200 395 255 345 L272 403 Z" fill="#e8a33e"/>
    <path d="M150 403 Q215 392 258 360 L268 403 Z" fill="#e07f2e"/>
    <path d="M150 403 Q200 396 240 385 L258 403 Z" fill="#555555"/>
    <path d="M255 345 Q275 385 330 403 L262 403 Z" fill="#e8a33e"/>
    <path d="M258 360 Q272 392 305 403 L264 403 Z" fill="#d2701d"/>
    <path d="M258 380 Q265 398 285 403 L258 403 Z" fill="#444444"/>
  </svg>

  <div class="panel panel--1">
    <h1 class="intro-title">
      <span class="intro-word">Landscaping</span>
      <span class="intro-to">To</span>
      <span class="intro-word">Your</span>
      <span class="intro-accent">LIFESTYLE</span>
    </h1>
  </div>

  <div class="panel panel--2">
    <h2 class="heading services-title">Our <em>Services</em></h2>
    <article class="service">
      <h3 class="heading service-name">Consultation and Design</h3>
      <p class="service-copy body-copy">The Halvorsen Group can work with you for a full landscape design concept or visit your site to discuss an existing plan.</p>
    </article>
    <article class="service">
      <h3 class="heading service-name">Earthwork and Site Preperation</h3>
      <p class="service-copy body-copy">Depending on the nature of the, it is imperative that your foundation and earth is well prepared for construction and planting. This will determine a quality outcome and the longevity we promote so you don't have issues in the future.</p>
    </article>
  </div>

  <div class="panel panel--3">
    <h2 class="heading services-title">Our <em>Services</em></h2>
    <article class="service">
      <h3 class="heading service-name">Installation and Construction</h3>
      <p class="service-copy body-copy">Upon a well prepared site, the Halvorsen Group are a professional landscape and construction company that works with a whole range of materials and structural designs.</p>
    </article>
    <article class="service">
      <h3 class="heading service-name">Maintenance Programs</h3>
      <p class="service-copy body-copy">We understand people can be 'caught up' or procrastinate in attending to landscape maintenance. Once you have invested in an outdoor project, its important it is retained for continuous enjoyment and longevity, and to avoid any costly neglect!</p>
    </article>
  </div>
</section>

</body>
</html>
```